business card and stationary pest control company
Bugwarden
business card and stationary pest control company - Cleaning
Creative Brief
Bright & Fun-filled
Malcolm Teague
General Manager
to be added
info@bugwarden.example
bugwarden.example
tarloq tarloq
Hi guys, please bear in mind it's a full stationary project, letterhead, fax, email, envelope etc ...
ravenmoss ravenmoss
check your private messages on top right! thankyou

```html
<!DOCTYPE html>
<html lang="en">
<head>
<meta charset="utf-8">
<title>Bugwarden business card</title>
<link href="https://fonts.googleapis.com/css2?family=Arimo:wght@400;700&display=swap" rel="stylesheet">
<style>
  :root {
    --backdrop: #2b2b2b;
    --card: #f4f4f4;
    --brand-blue: #1d3f8f;
    --brand-red: #d9242b;
    --ink: #333333;
    --muted: #666666;
  }
  * { margin: 0; padding: 0; box-sizing: border-box; }
  html, body { width: 1200px; height: 693px; overflow: hidden; }
  body {
    background: var(--backdrop);
    font-family: "Arimo", Arial, sans-serif;
    position: relative;
  }
  .card {
    position: absolute;
    width: 492px;
    height: 283px;
    background: var(--card);
    border-radius: 16px;
    overflow: hidden;
    box-shadow: 0 6px 18px rgba(0,0,0,.45);
  }
  .card-front { left: 216px; top: 29px; }
  .card-back { left: 475px; top: 336px; }
  .front-swoosh { position: absolute; inset: 0; width: 100%; height: 100%; }

  .brand { position: absolute; display: flex; align-items: center; gap: 8px; }
  .brand-dot { border-radius: 50%; background: var(--brand-red); flex: none; }
  .brand-name { color: var(--brand-blue); font-weight: 700; line-height: 1; letter-spacing: -0.5px; }

  .card-front .brand { left: 118px; top: 48px; }
  .card-front .brand-dot { width: 24px; height: 24px; }
  .card-front .brand-name { font-size: 30px; }

  .card-back .brand { left: 0; right: 0; top: 122px; justify-content: center; }
  .card-back .brand-dot { width: 28px; height: 28px; }
  .card-back .brand-name { font-size: 34px; }

  .holder { position: absolute; left: 120px; top: 118px; }
  .holder-name { color: var(--brand-blue); font-weight: 700; font-size: 21px; }
  .holder-role { color: var(--ink); font-size: 15px; margin-top: 3px; }

  .contacts { position: absolute; left: 120px; top: 186px; list-style: none; }
  .contacts li {
    display: flex; align-items: center; gap: 8px;
    color: var(--muted); font-size: 12.5px; height: 15px;
  }
  .contacts svg { width: 11px; height: 11px; flex: none; }
</style>
</head>
<body>
  <section class="card card-front" aria-label="Business card front">
    <svg class="front-swoosh" viewBox="0 0 492 283" preserveAspectRatio="none" aria-hidden="true">
      <path d="M0 0 H40 C34 90 50 200 110 283 H0 Z" fill="var(--brand-red)"/>
      <path d="M0 0 H30 C22 90 34 200 92 283 H0 Z" fill="var(--brand-blue)"/>
      <path d="M40 0 H46 C40 90 58 200 122 283 H110 C50 200 34 90 40 0 Z" fill="#ffffff"/>
    </svg>

    <div class="brand">
      <span class="brand-dot"></span>
      <div class="brand-name">Bugwarden</div>
    </div>

    <div class="holder">
      <div class="holder-name">Owen Hartley</div>
      <div class="holder-role">Founder</div>
    </div>

    <ul class="contacts">
      <li>
        <svg viewBox="0 0 12 12"><rect x="3" y="0.5" width="6" height="11" rx="1" fill="none" stroke="#555" stroke-width="1.2"/><circle cx="6" cy="9.5" r=".8" fill="#555"/></svg>
        020 555 0143
      </li>
      <li>
        <svg viewBox="0 0 12 12"><rect x="0.5" y="2" width="11" height="8" fill="#555"/><path d="M0.5 2 L6 7 L11.5 2" fill="none" stroke="#fff" stroke-width="1"/></svg>
        info@bugwarden.example
      </li>
      <li>
        <svg viewBox="0 0 12 12"><circle cx="6" cy="6" r="5.3" fill="none" stroke="#555" stroke-width="1.2"/><path d="M0.7 6 H11.3 M6 0.7 C3 4 3 8 6 11.3 M6 0.7 C9 4 9 8 6 11.3" fill="none" stroke="#555" stroke-width=".9"/></svg>
        www.bugwarden.example
      </li>
      <li>
        <svg viewBox="0 0 12 12"><circle cx="6" cy="6" r="5.5" fill="var(--brand-blue)"/></svg>
        @bugwarden
      </li>
    </ul>
  </section>

  <section class="card card-back" aria-label="Business card back">
    <div class="brand">
      <span class="brand-dot"></span>
      <div class="brand-name">Bugwarden</div>
    </div>
  </section>
</body>
</html>
```